LOCAL TAXI SERVICE NEEDS A BANNER AD DESIGN

NEED BANNER AD DESIGN FOR TAXI SERVICE IN NJ. WE PROVIDE LOCAL AND LONG DISTANCE TRANSPORTATION. OUR MAIN BASE OF CUSTOMER GO TO THE MAJOR AIRPORTS IN THE TRI STATE AREA. I WANT TO OFFER A SPECIAL GOING TO HOLMBRIDGE AIRPORT OF $35.00 WITH A COUPON CODE OF PW 12. THIS BANNER AD WILL BE USED FOR MY PALWIRE PAGE

Target Market(s)

PEOPLE WHO TRAVEL A LOT

Industry/Entity Type

Taxi

Font styles to use
Serif
Sans Serif

Colors
0792cd
0255a3
33a6d7
85cae6
cee9f5
ecf7fb
ffffff

Requirements
Must have
• MY COMPANY NAME: DORVAN'S TAXI

```html
<!DOCTYPE html>
<html lang="en">
<head>
<meta charset="utf-8">
<title>Dorvan's Taxi – Airport Special</title>
<link rel="stylesheet" href="https://fonts.googleapis.com/css2?family=Roboto+Condensed:wght@500;700;800&display=swap">
<style>
  :root {
    --blue-deep: #0255a3;
    --blue-mid: #0792cd;
    --blue-bright: #33a6d7;
    --blue-soft: #85cae6;
    --blue-pale: #cee9f5;
    --blue-mist: #ecf7fb;
    --white: #ffffff;
  }
  * { margin: 0; padding: 0; box-sizing: border-box; }
  html, body { width: 1200px; height: 1117px; overflow: hidden; background: var(--white); }
  .banner {
    position: relative;
    width: 1200px;
    height: 1117px;
    overflow: hidden;
    font-family: "Roboto Condensed", "Arial Narrow", sans-serif;
    background: linear-gradient(180deg, var(--white) 0%, var(--blue-mist) 40%, var(--blue-pale) 78%, var(--white) 100%);
  }
  .checker-band {
    position: absolute; left: 0; width: 1200px;
    background: linear-gradient(90deg, var(--blue-soft), var(--blue-pale), var(--blue-soft));
  }
  .checker-band--top { top: 0; height: 22px; }
  .checker-band--bottom { bottom: 0; height: 62px; }

  .brand {
    position: absolute; left: 68px; top: 58px;
    display: flex; align-items: center; gap: 26px;
  }
  .brand__square {
    width: 130px; height: 140px;
    border: 10px solid var(--blue-deep);
    border-radius: 8px;
    background: var(--white);
  }
  .brand__name {
    font-weight: 800; font-size: 150px; line-height: 1;
    color: var(--blue-deep); letter-spacing: 1px; white-space: nowrap;
  }

  .phone-band {
    position: absolute; left: 0; top: 229px; width: 1200px; height: 168px;
    background: var(--blue-deep);
    display: flex; align-items: center; justify-content: center;
  }
  .phone-band__number {
    color: var(--white); font-weight: 700; font-size: 140px; line-height: 1; letter-spacing: 2px;
  }

  .vehicle {
    position: absolute; left: 50px; top: 400px; width: 1100px; height: 470px;
    border-radius: 60px 60px 30px 30px;
    background: radial-gradient(ellipse at 50% 45%, #f7f9fb 0%, #d9dee3 55%, var(--blue-soft) 100%);
  }

  .offer {
    position: absolute; left: 0; top: 872px; width: 1200px; height: 180px;
  }
  .offer__shape { position: absolute; inset: 0; }
  .offer__route {
    position: absolute; left: 36px; top: 22px;
    color: var(--blue-deep); font-weight: 700; font-size: 68px; line-height: 0.98;
  }
  .offer__price {
    position: absolute; left: 540px; top: -12px;
    color: var(--white); font-weight: 800; font-size: 210px; line-height: 1;
  }
  .coupon {
    position: absolute; left: 880px; top: 18px; width: 290px; height: 146px;
    border: 5px solid var(--white);
    display: flex; flex-direction: column; align-items: center; padding: 8px 12px 12px;
  }
  .coupon__label {
    color: var(--white); font-weight: 700; font-size: 34px; line-height: 1.1; letter-spacing: 1px;
  }
  .coupon__code {
    margin-top: 8px; width: 100%; flex: 1;
    background: var(--white); color: var(--blue-deep);
    font-weight: 700; font-size: 58px; line-height: 1;
    display: flex; align-items: center; justify-content: center;
  }
</style>
</head>
<body>
  <main class="banner">
    <div class="checker-band checker-band--top" role="img" aria-label="Blue and white checkered taxi strip"></div>

    <header class="brand">
      <div class="brand__square"></div>
      <h1 class="brand__name">DORVAN'S TAXI</h1>
    </header>

    <div class="phone-band">
      <p class="phone-band__number">(973) 555-0147</p>
    </div>

    <div class="vehicle" role="img" aria-label="White minivan taxi with company name and phone number on the side door"></div>

    <section class="offer">
      <svg class="offer__shape" width="1200" height="180" viewBox="0 0 1200 180" aria-hidden="true">
        <rect x="0" y="0" width="1200" height="180" fill="var(--blue-soft)"/>
        <polygon points="560,0 1200,0 1200,180 500,180" fill="var(--blue-deep)"/>
      </svg>
      <p class="offer__route">TO HOLMBRIDGE<br>AIRPORT</p>
      <p class="offer__price">$35</p>
      <div class="coupon">
        <span class="coupon__label">COUPON CODE</span>
        <span class="coupon__code">PW 12</span>
      </div>
    </section>

    <div class="checker-band checker-band--bottom" role="img" aria-label="Blue and white checkered taxi strip"></div>
  </main>
</body>
</html>
```